BHSC Business cards

We are an established dental practice that is looking for new business cards to match our new logo. We are looking for something unique and sophisticated.
BRIEF: Colours are black, silver and white. Include the company name, logo (including “Pelwick Heath Dental Care”) and phone number “03 9415 2876”.
Front - Include the company name, logo (including “Pelwick Heath Dental Care”) and phone number “03 9415 2876”.
Back - Include the company name,  “Pelwick Heath Dental Care”, phone number “03 9415 2876”. address "64A Tindle Street, Pelwick Heath, Vic 3187", "Email reception@pelwickheathdentalcare.com.au", the Dentist Name " Dr ................................"  Your next appointment "Day, date and time(am/pm)".  3 lines for 3 appointments please, and at the bottom "IF UNABLE TO KEEP THIS APPOINTMENT 48 HOURS NOTICE IS REQUIRED."
Try and be creative and different with the design, i've added an image for inspiration

Target Market(s)
ALL in need of dental
Industry/Entity Type
Dental Clinic
Look and feel
Each slider illustrates characteristics of the customer's brand and the style your logo design should communicate.

```html
<!DOCTYPE html>
<html lang="en">
<head>
<meta charset="utf-8">
<title>Pelwick Heath Dental Care – Business Cards</title>
<link href="https://fonts.googleapis.com/css2?family=Arimo:wght@400;700&display=swap" rel="stylesheet">
<style>
  :root {
    --stage: #2b2b2d;
    --card-black: #1c1a1b;
    --card-edge: #0d0c0c;
    --white: #ffffff;
    --silver: #c9c9cc;
    --ink: #1a1a1a;
  }
  * { box-sizing: border-box; margin: 0; padding: 0; }
  html, body {
    width: 1200px; height: 900px; overflow: hidden;
    background: var(--stage);
    font-family: "Arimo", Arial, sans-serif;
  }
  .canvas {
    position: relative; width: 1200px; height: 900px;
  }
  .card {
    position: absolute;
    width: 640px; height: 390px;
    left: 280px;
    background: linear-gradient(160deg, #2a2728 0%, var(--card-black) 55%, var(--card-edge) 100%);
    border-radius: 26px;
    color: var(--white);
  }
  .card--appointment { top: 45px; }
  .card--contact { top: 465px; }

  /* brand lockup */
  .brand {
    display: flex; align-items: center; gap: 14px;
  }
  .brand__mark {
    width: 44px; height: 44px; border-radius: 50%;
    border: 3px solid var(--white); flex: none;
  }
  .brand__name {
    font-weight: 700; font-size: 22px; letter-spacing: 2px;
    text-transform: uppercase; line-height: 1.05; color: var(--white);
  }

  /* appointment side */
  .appointment__head {
    position: absolute; left: 150px; top: 28px;
  }
  .appointment__label {
    font-size: 16px; letter-spacing: 0.5px; margin: 6px 0 0 58px;
  }
  .appointment__panel {
    position: absolute; left: 34px; right: 34px; top: 118px; height: 176px;
    background: var(--white); color: var(--ink);
    border-radius: 18px; padding: 16px 28px 0;
  }
  .appointment__rule {
    border-bottom: 2px dotted var(--ink); height: 14px; margin-bottom: 12px;
  }
  .appointment__row {
    display: flex; align-items: baseline; font-size: 17px; margin-bottom: 18px;
  }
  .appointment__row span { flex: none; }
  .appointment__dots {
    flex: 1; border-bottom: 2px dotted var(--ink); margin: 0 4px; transform: translateY(-3px);
  }
  .appointment__dots--short { flex: 0.8; }
  .appointment__notice {
    position: absolute; left: 0; right: 0; bottom: 26px;
    text-align: center; font-size: 17px; letter-spacing: 0.5px; line-height: 1.25;
    text-transform: uppercase;
  }

  /* contact side */
  .contact__brand {
    position: absolute; left: 0; right: 0; top: 42px; justify-content: center;
  }
  .contact__brand .brand__mark { width: 58px; height: 58px; }
  .contact__brand .brand__name { font-size: 25px; }
  .contact__person {
    position: absolute; left: 0; right: 0; top: 138px; text-align: center;
  }
  .contact__name {
    font-weight: 700; font-size: 24px; letter-spacing: 1.5px; text-transform: uppercase;
  }
  .contact__role { font-size: 15px; color: var(--silver); margin-top: 2px; }
  .contact__details {
    position: absolute; left: 60px; right: 60px; top: 222px; text-align: center;
    font-size: 20px; line-height: 1.35;
  }
  .contact__rule {
    height: 2px; background: var(--silver); margin: 10px 20px 10px;
  }
</style>
</head>
<body>
<main class="canvas">

  <section class="card card--appointment" aria-label="Appointment card">
    <div class="appointment__head">
      <div class="brand">
        <span class="brand__mark"></span>
        <span class="brand__name">Pelwick Heath Dental Care</span>
      </div>
      <p class="appointment__label">Your next appointment</p>
    </div>

    <div class="appointment__panel">
      <div class="appointment__rule"></div>
      <div class="appointment__row">
        <span>Day</span><i class="appointment__dots"></i>
        <span>Date</span><i class="appointment__dots"></i>
        <span>Time</span><i class="appointment__dots appointment__dots--short"></i>
        <span>am / pm</span>
      </div>
      <div class="appointment__row">
        <span>Day</span><i class="appointment__dots"></i>
        <span>Date</span><i class="appointment__dots"></i>
        <span>Time</span><i class="appointment__dots appointment__dots--short"></i>
        <span>am / pm</span>
      </div>
      <div class="appointment__row">
        <span>Day</span><i class="appointment__dots"></i>
        <span>Date</span><i class="appointment__dots"></i>
        <span>Time</span><i class="appointment__dots appointment__dots--short"></i>
        <span>am / pm</span>
      </div>
    </div>

    <p class="appointment__notice">If unable to keep this appointment<br>48 hours notice is required</p>
  </section>

  <section class="card card--contact" aria-label="Contact card">
    <div class="brand contact__brand">
      <span class="brand__mark"></span>
      <span class="brand__name">Pelwick Heath Dental Care</span>
    </div>
    <div class="contact__person">
      <p class="contact__name">Marcus Ellery</p>
      <p class="contact__role">Manager</p>
    </div>
    <div class="contact__details">
      <p class="contact__phone">03 9415 2876</p>
      <p class="contact__email">reception@pelwickheathdentalcare.com.au</p>
      <div class="contact__rule"></div>
      <p class="contact__address">64A Tindle Street, Pelwick Heath, Vic 3187</p>
    </div>
  </section>

</main>
</body>
</html>
```